Website for Healthy Energy Bars

I need the layout for a website that will allow customers to purchase three different energy bars. It should have a slide show of pictures on the front page and the following tabs: About, Nutrition Info, FAQ

The website colors should not conflict with the colors of the company logo. Other than that I am open to design ideas and concepts.

Target Market(s)

Health-Conscious Eaters

Industry/Entity Type

Purchase

Number of Pages Required

3 page

Requirements
Must have
• Logo and pictures of the product
Should not have
• Colors that conflict with the logo colors

```html
<!DOCTYPE html>
<html lang="en">
<head>
<meta charset="utf-8">
<title>Leafwell — Energy Bars</title>
<link rel="stylesheet" href="https://fonts.googleapis.com/css2?family=Roboto:wght@300;400;500;700&display=swap">
<style>
  :root {
    --green: #8cc63f;
    --green-dark: #6fa82a;
    --ink: #4a4a4a;
    --ink-soft: #7a7a7a;
    --line: #e2e2e2;
    --panel: #f2f2f2;
    --panel-light: #fafafa;
    --white: #ffffff;
    --brand-dark: #4a2a2e;
  }
  * { box-sizing: border-box; margin: 0; padding: 0; }
  html, body { width: 1200px; height: 2920px; overflow: hidden; }
  body {
    background: var(--white);
    font-family: "Roboto", Helvetica, Arial, sans-serif;
    color: var(--ink);
    position: relative;
  }
  .brand {
    display: flex; align-items: center; justify-content: center; gap: 12px;
    font-weight: 700; font-size: 44px; color: var(--green); letter-spacing: -0.5px;
  }
  .brand-dot { width: 22px; height: 22px; border-radius: 50%; background: var(--green); }

  .site-header { position: absolute; top: 0; left: 0; width: 1200px; height: 228px; }
  .site-header .brand { position: absolute; top: 48px; left: 0; width: 100%; }
  .main-nav {
    position: absolute; top: 188px; left: 220px; width: 760px; height: 30px;
    border-top: 1px solid var(--line); border-bottom: 1px solid var(--line);
    display: flex; align-items: center; padding: 0 14px; gap: 30px;
    font-size: 11px; letter-spacing: 0.6px; color: var(--ink-soft);
  }
  .main-nav .active { color: var(--green); }
  .nav-search { margin-left: auto; display: flex; align-items: center; gap: 10px; }
  .nav-search input {
    width: 150px; height: 18px; border: 1px solid var(--line); font-size: 10px;
  }

  .hero { position: absolute; top: 228px; left: 0; width: 1200px; height: 500px; background: var(--panel); }
  .hero-box {
    position: absolute; left: 360px; top: 70px; width: 300px; height: 300px;
    background: linear-gradient(160deg, #e8f2da, #b9d88a 60%, #6b4a3a);
    border-radius: 6px;
  }
  .hero-bites {
    position: absolute; left: 600px; top: 170px; width: 340px; height: 200px;
    background: radial-gradient(ellipse at center, #f1e3c4 0%, #e6d3ad 55%, rgba(242,242,242,0) 75%);
  }
  .hero-copy { position: absolute; left: 740px; top: 110px; width: 260px; text-align: center; }
  .hero-copy h1 { font-weight: 300; font-size: 44px; line-height: 1.2; color: var(--ink); }
  .btn {
    display: inline-block; background: var(--green); color: var(--white);
    font-size: 11px; font-weight: 500; letter-spacing: 0.8px; padding: 10px 22px;
  }
  .hero-copy .btn { margin-top: 40px; }
  .hero-arrow { position: absolute; top: 236px; width: 28px; height: 28px; }
  .hero-arrow.prev { left: 14px; }
  .hero-arrow.next { right: 14px; }

  .products { position: absolute; top: 752px; left: 20px; width: 1160px; }
  .product-row { display: flex; height: 564px; margin-bottom: 4px; }
  .product-photo {
    width: 580px; height: 100%; background: var(--panel); position: relative;
  }
  .product-photo .pack {
    position: absolute; left: 150px; top: 190px; width: 280px; height: 180px; border-radius: 8px;
    background: linear-gradient(135deg, #eef3e6, #d9c49a 55%, #9a6b45);
  }
  .product-info {
    width: 580px; height: 100%; background: var(--panel-light);
    display: flex; flex-direction: column; align-items: center; justify-content: center; text-align: center;
    padding: 0 110px;
  }
  .product-info h2 { font-weight: 300; font-size: 40px; line-height: 1.15; color: var(--ink); }
  .product-tags { margin-top: 24px; font-size: 9px; letter-spacing: 0.4px; color: var(--ink); }
  .product-desc { margin-top: 14px; font-size: 11px; line-height: 1.55; color: var(--ink-soft); }
  .product-info .btn { margin-top: 28px; padding: 10px 40px; }

  .actions { position: absolute; top: 2512px; left: 0; width: 1200px; display: flex; justify-content: center; gap: 40px; }
  .btn-outline {
    width: 200px; height: 40px; border: 1px solid var(--green); color: var(--green);
    font-size: 11px; letter-spacing: 0.8px; display: flex; align-items: center; justify-content: center;
  }

  .site-footer { position: absolute; top: 2618px; left: 0; width: 1200px; height: 302px; border-top: 1px solid var(--line); }
  .site-footer .brand { position: absolute; top: 70px; left: 0; width: 100%; }
  .footer-nav {
    position: absolute; top: 196px; left: 0; width: 100%;
    display: flex; justify-content: center; gap: 26px; font-size: 10px; letter-spacing: 0.6px; color: var(--ink-soft);
  }
  .footer-legal { position: absolute; top: 222px; width: 100%; text-align: center; font-size: 9px; color: var(--ink-soft); line-height: 1.6; }
</style>
</head>
<body>

<header class="site-header">
  <div class="brand"><span class="brand-dot"></span>Leafwell</div>
  <nav class="main-nav">
    <span class="active">HOME</span><span>ABOUT US</span><span>NUTRITION INFO</span><span>FAQ</span><span>CONTACT</span>
    <span class="nav-search">
      <svg width="12" height="12" viewBox="0 0 12 12"><circle cx="5" cy="5" r="3.6" fill="none" stroke="#9a9a9a" stroke-width="1.4"/><line x1="7.7" y1="7.7" x2="11" y2="11" stroke="#9a9a9a" stroke-width="1.4"/></svg>
      <input type="text" aria-label="Search">
    </span>
  </nav>
</header>

<section class="hero">
  <div class="hero-box" role="img" aria-label="Display box of energy bars with one wrapped bar in front"></div>
  <div class="hero-bites" role="img" aria-label="Scattered bite-sized energy bar pieces"></div>
  <div class="hero-copy">
    <h1>All Natural and Satisfying</h1>
    <span class="btn">VIEW OUR PRODUCTS</span>
  </div>
  <svg class="hero-arrow prev" viewBox="0 0 28 28"><circle cx="14" cy="14" r="13" fill="#c9dfa9"/><path d="M16 8 L10 14 L16 20" fill="none" stroke="#fff" stroke-width="2.4"/></svg>
  <svg class="hero-arrow next" viewBox="0 0 28 28"><circle cx="14" cy="14" r="13" fill="#c9dfa9"/><path d="M12 8 L18 14 L12 20" fill="none" stroke="#fff" stroke-width="2.4"/></svg>
</section>

<main class="products">
  <article class="product-row">
    <div class="product-photo"><div class="pack" role="img" aria-label="Wrapped coconut cashew chew bar"></div></div>
    <div class="product-info">
      <h2>Coconut Cashew Chew Bar</h2>
      <p class="product-tags">DAIRY FREE | GLUTEN FREE | VEGAN | GOOD SOURCE OF PROTEIN</p>
      <p class="product-desc">Lorem ipsum. Proin gravida nibh vel velit auctor aliquet. Aenean sollicitudin, lorem quis bibendum auctor, nisi elit consequat ipsum, nec sagittis sem nibh id elit. Duis sed odio sit amet nibh vulputate cursus a sit amet mauris.</p>
      <span class="btn">BUY NOW</span>
    </div>
  </article>
  <article class="product-row">
    <div class="product-info">
      <h2>Cherry Cashew Crunch Bar</h2>
      <p class="product-tags">DAIRY FREE | GLUTEN FREE | VEGAN | GOOD SOURCE OF PROTEIN</p>
      <p class="product-desc">Lorem ipsum. Proin gravida nibh vel velit auctor aliquet. Aenean sollicitudin, lorem quis bibendum auctor, nisi elit consequat ipsum, nec sagittis sem nibh id elit. Duis sed odio sit amet nibh vulputate cursus a sit amet mauris.</p>
      <span class="btn">BUY NOW</span>
    </div>
    <div class="product-photo"><div class="pack" role="img" aria-label="Wrapped cherry cashew crunch bar" style="background:linear-gradient(135deg,#f2f2ec,#e7d9a8 55%,#b85a4a)"></div></div>
  </article>
  <article class="product-row">
    <div class="product-photo"><div class="pack" role="img" aria-label="Wrapped chocolate almond crunch bar" style="background:linear-gradient(135deg,#eef3e6,#a88a5e 50%,#5a3a28)"></div></div>
    <div class="product-info">
      <h2>Chocolate Almond Crunch Bar</h2>
      <p class="product-tags">DAIRY FREE | GLUTEN FREE | VEGAN | GOOD SOURCE OF PROTEIN</p>
      <p class="product-desc">Lorem ipsum. Proin gravida nibh vel velit auctor aliquet. Aenean sollicitudin, lorem quis bibendum auctor, nisi elit consequat ipsum, nec sagittis sem nibh id elit. Duis sed odio sit amet nibh vulputate cursus a sit amet mauris.</p>
      <span class="btn">BUY NOW</span>
    </div>
  </article>
</main>

<div class="actions">
  <span class="btn-outline">NEWSLETTER</span>
  <span class="btn-outline">GO TO CART</span>
</div>

<footer class="site-footer">
  <div class="brand"><span class="brand-dot"></span>Leafwell</div>
  <nav class="footer-nav"><span>HOME</span><span>ABOUT US</span><span>NUTRITION INFO</span><span>FAQ</span><span>CONTACT</span></nav>
  <p class="footer-legal">© Copyright 2017 Leafwell Inc. | All Rights Reserved | Terms | Privacy<br>Website by Leafwell Studio</p>
</footer>

</body>
</html>
```